Oil and Gas Exploration and Production company needs a business card design

We need a business card design using our logo and colors in the logo. We want a mainstream design.

```html
<!DOCTYPE html>
<html lang="en">
<head>
<meta charset="utf-8">
<title>Condor Oil &amp; Gas – Business Card</title>
<link rel="stylesheet" href="https://fonts.googleapis.com/css2?family=Arimo:wght@700&family=Tinos:wght@400;700&display=swap">
<style>
  :root {
    --gold: #c9972f;
    --gold-light: #d8a943;
    --ink: #141414;
    --paper: #ffffff;
    --stage: #e6e6e6;
    --grey-text: #2a2a2a;
  }
  * { box-sizing: border-box; margin: 0; padding: 0; }
  html, body { width: 1200px; height: 906px; overflow: hidden; }
  body {
    background: var(--stage);
    display: flex;
    align-items: center;
    justify-content: center;
    gap: 40px;
    font-family: "Tinos", "Times New Roman", serif;
  }
  .card {
    width: 540px;
    height: 309px;
    border-radius: 16px;
    position: relative;
    overflow: hidden;
    box-shadow: 0 6px 18px rgba(0,0,0,0.18);
  }
  /* Back */
  .card-back {
    background: var(--gold);
    display: flex;
    align-items: center;
    justify-content: center;
  }
  .brand {
    display: flex;
    align-items: center;
    gap: 10px;
    font-family: "Tinos", "Times New Roman", serif;
    font-weight: 700;
    white-space: nowrap;
  }
  .brand-dot {
    width: 22px; height: 22px; border-radius: 50%;
  }
  .card-back .brand { color: var(--paper); font-size: 40px; }
  .card-back .brand-dot { background: var(--paper); }

  /* Front */
  .card-front { background: var(--paper); }
  .card-front .brand {
    position: absolute; top: 34px; right: 30px;
    color: var(--ink); font-size: 30px;
  }
  .card-front .brand-dot { background: var(--ink); width: 18px; height: 18px; }
  .holder {
    position: absolute; left: 30px; top: 112px;
  }
  .holder-name {
    font-family: "Arimo", Arial, sans-serif;
    font-weight: 700; font-size: 21px; color: var(--ink);
    letter-spacing: 0.3px;
  }
  .holder-role {
    font-size: 15px; color: var(--gold); margin-top: 1px;
  }
  .contacts {
    position: absolute; left: 30px; top: 178px;
    list-style: none;
  }
  .contacts li {
    display: flex; align-items: center; gap: 12px;
    font-size: 15px; color: var(--grey-text);
    height: 26px;
  }
  .contact-icon {
    width: 20px; height: 20px; border-radius: 50%;
    background: var(--ink);
    display: flex; align-items: center; justify-content: center;
    flex: none;
  }
  .address {
    position: absolute; right: 30px; top: 150px;
    text-align: right; font-size: 15px; line-height: 1.35;
    color: var(--grey-text);
  }
  .base-band {
    position: absolute; left: 0; bottom: 0; width: 540px; height: 60px;
  }
</style>
</head>
<body>

  <section class="card card-back" aria-label="Card back">
    <div class="brand"><span class="brand-dot"></span>Condor Oil &amp; Gas</div>
  </section>

  <section class="card card-front" aria-label="Card front">
    <div class="brand"><span class="brand-dot"></span>Condor Oil &amp; Gas</div>

    <div class="holder">
      <p class="holder-name">DANIEL MORENO</p>
      <p class="holder-role">Managing Director</p>
    </div>

    <ul class="contacts">
      <li>
        <span class="contact-icon">
          <svg width="11" height="11" viewBox="0 0 24 24"><path fill="#c9972f" d="M6.6 10.8a15 15 0 0 0 6.6 6.6l2.2-2.2a1 1 0 0 1 1-.25 11.4 11.4 0 0 0 3.6.57 1 1 0 0 1 1 1V20a1 1 0 0 1-1 1A17 17 0 0 1 3 4a1 1 0 0 1 1-1h3.5a1 1 0 0 1 1 1c0 1.25.2 2.45.57 3.6a1 1 0 0 1-.25 1z"/></svg>
        </span>555.014.2290
      </li>
      <li>
        <span class="contact-icon">
          <svg width="12" height="10" viewBox="0 0 24 18"><rect x="1" y="1" width="22" height="16" fill="#c9972f"/><path d="M1 1l11 9 11-9" fill="none" stroke="#141414" stroke-width="2"/></svg>
        </span>daniel@condoroilgas.com
      </li>
      <li>
        <span class="contact-icon">
          <svg width="12" height="12" viewBox="0 0 24 24" fill="none" stroke="#c9972f" stroke-width="2"><circle cx="12" cy="12" r="10"/><ellipse cx="12" cy="12" rx="4.5" ry="10"/><path d="M2 12h20M4 6.5h16M4 17.5h16"/></svg>
        </span>www.condoroilgas.com
      </li>
    </ul>

    <address class="address" style="font-style:normal">
      82 Harlow Street<br>
      Riverton, California 94000
    </address>

    <svg class="base-band" viewBox="0 0 540 60" preserveAspectRatio="none" aria-hidden="true">
      <polygon points="0,44 470,14 488,6 540,6 540,60 0,60" fill="var(--ink)"/>
      <polygon points="0,42 474,12 490,2 494,2 478,15 0,48" fill="var(--gold)"/>
    </svg>
  </section>

</body>
</html>
```